Business cards Marta Keller Sport & Events

I need new business cards to match my new logo design for my company called "Marta Keller Sport & Events". I'm based in Germany.
With my company, I offer different services in the context of sport.

Marta Keller owner

Marta Keller Sports & Events
Birkendorfer Weg 14
D-63158 Offenbach

+49 69 / 31 52 94 07
info@marta-keller-sport.example
www.marta-keller-sport.example

Contact Information for Business Card

Marta Keller Inhaberin Marta Keller Sport & Events Birkendorfer Weg 14 D-63158 Offenbach +49 69 / 31 52 94 07 info@marta-keller-sport.example www.marta-keller-sport.example

Requirements
Must have
• Logo | Double sided business card

```html
<!DOCTYPE html>
<html lang="en">
<head>
<meta charset="utf-8">
<title>Marta Keller Sport &amp; Events – Business Card</title>
<link rel="stylesheet" href="https://fonts.googleapis.com/css2?family=Arimo:wght@400;600&family=Michroma&display=swap">
<style>
  :root {
    --bg: #c9c9c9;
    --card-white: #ffffff;
    --brand-orange: #f9a31d;
    --emboss-gold: #c48d12;
    --ink: #1c1c1c;
    --divider: #e2e2e2;
  }
  * { box-sizing: border-box; margin: 0; padding: 0; }
  html, body { width: 1200px; height: 800px; overflow: hidden; }
  body {
    background: var(--bg);
    font-family: "Arimo", Arial, sans-serif;
    color: var(--ink);
    position: relative;
  }
  .card {
    position: absolute;
    top: 245px;
    width: 540px;
    height: 310px;
    box-shadow: 0 14px 30px rgba(0,0,0,.25);
  }
  .card--front { left: 40px; background: var(--card-white); display: flex; }
  .card--back {
    left: 620px;
    background: var(--brand-orange);
    display: flex;
    align-items: center;
    justify-content: center;
  }
  .brand-area {
    width: 50%;
    display: flex;
    align-items: center;
    justify-content: center;
    gap: 10px;
    border-right: 1px solid var(--divider);
  }
  .brand-mark {
    width: 30px; height: 30px; border-radius: 50%;
    background: var(--brand-orange);
    flex: none;
  }
  .brand-name {
    font-weight: 600;
    font-size: 16px;
    color: var(--ink);
    white-space: nowrap;
  }
  .contact-area {
    width: 50%;
    padding: 58px 0 0 26px;
    font-size: 12px;
    line-height: 1.35;
  }
  .contact-name {
    font-family: "Michroma", sans-serif;
    font-size: 17px;
    color: var(--brand-orange);
    letter-spacing: 1px;
    line-height: 1.1;
  }
  .contact-role { font-size: 13px; margin-bottom: 12px; }
  .contact-list { list-style: none; margin-bottom: 12px; }
  .contact-list li { display: flex; align-items: center; gap: 6px; }
  .contact-list svg { width: 12px; height: 12px; flex: none; }
  .company-name { color: var(--brand-orange); font-size: 13px; }
  .address { font-size: 13px; font-style: normal; }
  .back-brand { display: flex; align-items: center; gap: 16px; }
  .back-brand .brand-mark { width: 54px; height: 54px; background: var(--emboss-gold); }
  .back-brand .brand-name { font-size: 26px; color: var(--emboss-gold); }
</style>
</head>
<body>
  <section class="card card--front" aria-label="Business card front">
    <div class="brand-area">
      <span class="brand-mark" aria-hidden="true"></span>
      <span class="brand-name">Marta Keller Sport &amp; Events</span>
    </div>
    <div class="contact-area">
      <h1 class="contact-name">MARTA KELLER</h1>
      <p class="contact-role">Owner</p>
      <ul class="contact-list">
        <li>
          <svg viewBox="0 0 12 12" aria-hidden="true"><path d="M2.5 1 4.5 1 5.2 3.6 4 4.6a6 6 0 0 0 3.4 3.4l1-1.2 2.6.7V9.5A1.5 1.5 0 0 1 9.5 11 8.5 8.5 0 0 1 1 2.5 1.5 1.5 0 0 1 2.5 1z" fill="#f9a31d"/></svg>
          +49 69 / 31 52 94 07
        </li>
        <li>
          <svg viewBox="0 0 12 12" aria-hidden="true"><rect x="1" y="2.5" width="10" height="7" fill="#f9a31d"/><path d="M1 2.5 6 6.5 11 2.5" stroke="#fff" stroke-width="1" fill="none"/></svg>
          info@marta-keller-sport.example
        </li>
        <li>
          <svg viewBox="0 0 12 12" aria-hidden="true"><circle cx="6" cy="6" r="5" fill="#f9a31d"/><path d="M1 6h10M6 1c-2.5 3-2.5 7 0 10M6 1c2.5 3 2.5 7 0 10" stroke="#fff" stroke-width=".8" fill="none"/></svg>
          www.marta-keller-sport.example
        </li>
      </ul>
      <p class="company-name">Marta Keller Sports &amp; Events</p>
      <address class="address">Birkendorfer Weg 14<br>D-63158 Offenbach</address>
    </div>
  </section>

  <section class="card card--back" aria-label="Business card back">
    <div class="back-brand">
      <span class="brand-mark" aria-hidden="true"></span>
      <span class="brand-name">Marta Keller Sport &amp; Events</span>
    </div>
  </section>
</body>
</html>
```